Solar appointment reminder card

We are looking for a new design for our appointment reminder card since we have changed our logo. The card should have the new logo along with space for the employee to hand write the customers appointment date, time, the employees name and phone number.
I've uploaded what our old basic appointment card looked like and our new logo.

The cards should be in a standard business card size and could be horizontal or vertical.

```html
<!DOCTYPE html>
<html lang="en">
<head>
<meta charset="utf-8">
<title>Hudson Ray Energy – Appointment Card</title>
<link href="https://fonts.googleapis.com/css2?family=Montserrat:wght@800&family=Open+Sans:ital,wght@0,700;1,400;1,600&display=swap" rel="stylesheet">
<style>
  :root {
    --ink: #000000;
    --paper: #ffffff;
    --orange: #f39023;
    --sun: #fdc62b;
    --rule: #9a9a9a;
  }
  html, body {
    margin: 0;
    padding: 0;
    width: 1003px;
    height: 1200px;
    overflow: hidden;
    background: var(--paper);
  }
  .canvas { position: relative; width: 1003px; height: 1200px; }

  .card {
    position: absolute;
    left: 120px;
    width: 763px;
    height: 437px;
    box-sizing: border-box;
  }
  .card--front { top: 88px; background: var(--ink); }
  .card--back { top: 643px; background: var(--paper); border: 3px solid var(--ink); }

  .side-label {
    position: absolute;
    left: 122px;
    margin: 0;
    font-family: "Open Sans", sans-serif;
    font-style: italic;
    font-weight: 400;
    font-size: 21px;
    color: var(--ink);
  }
  .side-label--front { top: 533px; }
  .side-label--back { top: 1095px; }

  .brand { position: absolute; display: flex; align-items: center; }
  .brand__dot { border-radius: 50%; background: var(--sun); flex: none; }
  .brand__name {
    margin: 0;
    font-family: "Montserrat", sans-serif;
    font-weight: 800;
    color: var(--orange);
    line-height: 1.02;
    letter-spacing: 0.01em;
  }

  .brand--large { left: 90px; top: 140px; }
  .brand--large .brand__dot { width: 150px; height: 150px; margin-right: 40px; }
  .brand--large .brand__name { font-size: 60px; }

  .back-panel {
    position: absolute;
    left: -3px; top: -3px; bottom: -3px;
    width: 290px;
    background: var(--ink);
  }
  .brand--small { left: 10px; bottom: 70px; }
  .brand--small .brand__dot { width: 64px; height: 64px; margin-right: 14px; }
  .brand--small .brand__name { font-size: 26px; }

  .appointment-band {
    position: absolute;
    left: 284px; top: 48px;
    width: 441px; height: 33px;
    background: var(--orange);
    margin: 0;
    font-family: "Open Sans", sans-serif;
    font-weight: 700;
    font-size: 22px;
    line-height: 33px;
    letter-spacing: 0.03em;
    text-align: center;
    color: var(--paper);
  }

  .field { position: absolute; left: 297px; width: 428px; height: 24px; }
  .field__label {
    position: absolute; left: 0; bottom: 0;
    font-family: "Open Sans", sans-serif;
    font-style: italic;
    font-weight: 600;
    font-size: 16px;
    color: var(--orange);
  }
  .field__line {
    position: absolute; left: 124px; right: 0; bottom: 2px;
    border-top: 1.5px solid var(--rule);
  }
  .field--date { top: 124px; }
  .field--time { top: 196px; }
  .field--rep { top: 269px; }
  .field--phone { top: 342px; }
</style>
</head>
<body>
<div class="canvas">

  <section class="card card--front">
    <div class="brand brand--large">
      <span class="brand__dot"></span>
      <p class="brand__name">HUDSON RAY<br>ENERGY</p>
    </div>
  </section>
  <p class="side-label side-label--front">front</p>

  <section class="card card--back">
    <div class="back-panel">
      <div class="brand brand--small">
        <span class="brand__dot"></span>
        <p class="brand__name">HUDSON RAY<br>ENERGY</p>
      </div>
    </div>
    <h2 class="appointment-band">Appointment</h2>
    <div class="field field--date"><span class="field__label">Date:</span><span class="field__line"></span></div>
    <div class="field field--time"><span class="field__label">Time:</span><span class="field__line"></span></div>
    <div class="field field--rep"><span class="field__label">Representative:</span><span class="field__line"></span></div>
    <div class="field field--phone"><span class="field__label">Phone:</span><span class="field__line"></span></div>
  </section>
  <p class="side-label side-label--back">back</p>

</div>
</body>
</html>
```